Indie author needs a minimalist book cover

I need a book cover for my latest book on personal finance and investing. The book is called, "The Quiet Harvest: Methods for Steady Savings, Careful Spending, and a Calm Future". This is volume one of a three part series on the FI/RE movement, which stands for 'Financial Independence/Retire Early'. This book is on the foundational principles of FI/RE and details the specific steps that these 'Quiet Harvest' involved in this community have done to position themselves to retire from paid work and live the life of their dreams - many only in their 20's, 30's and early 40's.

Title: The Quiet Harvest
Author: PK Brenner
Volume 1: Foundations
Book dimensions: 6"x9"

Book Blurb (for back cover):

Let's face it, no one wants to be different. But sometimes following the 'normal' crowd gets you no further than that crowd.

When it comes to money, the normal crowd is your typical consumer. Deep in debt, struggling to make ends meet, but still spending money on the newest 'thing' that just came out.

But there's another group that's been forming - right on the fringes of the personal finance world. I call them The Quiet Harvest. This book is about these superheroes of personal finance.

In it, you will learn:
• Who The Quiet Harvest are and what is this FI/RE Movement they are apart of
• What basic strategy they use to control their money
• How they became debt-free - and how you can join them
• How to use the SP/CE Lever to help you really move the needle towards financial independence
• How to diversify your income with a side-hustle and which one to choose
• The money outlier savings plan that will allow you to reach financial independence in ten years or less

This first book in The Quiet Harvest series is about building a solid foundation so you and your family can become Quiet Harvest, reach financial freedom, retire early, and live a rich life.

Target Market(s)

Individuals looking to take control of their money, reach financial independence, and retire early.

Font styles to use
Sans Serif
Other font styles liked:
• Arvo

Colors

Designer to choose colors to be used in the design.

Requirements
Must have
• A minimalist design (see examples), the title of the book, my author name, and the volume number and name (see below).
• My vision for the cover is to have a way to represent an 'outlier' in a simple, minimalistic way. I'm not set on any specific design - I'm open to what the designers come up with; I don't want to hold back anyone's creativity.
• Title: The Quiet Harvest
• Author: PK Brenner
• Volume 1: Foundations
• Book Blurb (for back cover):
• Let's face it, no one wants to be different. But sometimes following the 'normal' crowd gets you no further than that crowd.
• When it comes to money, the normal crowd is your typical consumer. Deep in debt, struggling to make ends meet, but still spending money on the newest 'thing' that just came out.
• But there's another group that's been forming - right on the fringes of the personal finance world. I call them The Quiet Harvest. This book is about these superheroes of personal finance.
• In it, you will learn:
• • Who The Quiet Harvest are and what is this FI/RE Movement they are apart of
• • What basic strategy they use to control their money
• • How they became debt-free - and how you can join them
• • How to use the SP/CE Lever to help you really move the needle towards financial independence
• • How to diversify your income with a side-hustle and which one to choose
• • The money outlier savings plan that will allow you to reach financial independence in ten years or less
• This first book in The Quiet Harvest series is about building a solid foundation so you and your family can become Quiet Harvest, reach financial freedom, retire early, and live a rich life.
Nice to have
• The subtitle - but only if it's not too crowded. Like I said before, I'm more interested in maintaining a minimalist aesthetic.
• The subtitle is: "Methods for Steady Savings, Careful Spending, And A Calm Future"
Should not have
• Too many colors or objects on the cover.

```html
<!DOCTYPE html>
<html lang="en">
<head>
<meta charset="utf-8">
<title>The Quiet Harvest — Volume 1: Foundations</title>
<link rel="stylesheet" href="https://fonts.googleapis.com/css2?family=Arvo:wght@700&family=Roboto+Slab:wght@400&family=Crimson+Text&display=swap">
<style>
  :root {
    --paper: #f2e6d6;
    --ink: #555555;
    --ink-soft: #4a4a4a;
    --art-main: #c9d3c8;
    --art-edge: #eadfcf;
  }
  html, body {
    margin: 0;
    padding: 0;
    overflow: hidden;
  }
  .cover {
    position: relative;
    width: 800px;
    height: 1200px;
    background: var(--paper);
    overflow: hidden;
  }
  .cover-illustration {
    position: absolute;
    left: 200px;
    top: 150px;
    width: 360px;
    height: 560px;
    border-radius: 180px 180px 40px 40px;
    background: radial-gradient(ellipse at 50% 45%, var(--art-main) 0%, var(--art-edge) 75%, var(--paper) 100%);
  }
  .title {
    position: absolute;
    left: 0;
    right: 0;
    top: 762px;
    margin: 0;
    text-align: center;
    font-family: "Arvo", serif;
    font-weight: 700;
    font-size: 78px;
    line-height: 68px;
    letter-spacing: 1px;
    color: var(--ink);
    text-transform: uppercase;
  }
  .subtitle {
    position: absolute;
    left: 0;
    right: 0;
    top: 906px;
    margin: 0;
    text-align: center;
    font-family: "Roboto Slab", serif;
    font-size: 17px;
    color: var(--ink);
  }
  .volume {
    position: absolute;
    left: 0;
    right: 0;
    top: 1050px;
    margin: 0;
    text-align: center;
    font-family: "Crimson Text", serif;
    font-size: 24px;
    color: var(--ink-soft);
  }
  .author {
    position: absolute;
    left: 0;
    right: 0;
    top: 1092px;
    margin: 0;
    text-align: center;
    font-family: "Crimson Text", serif;
    font-size: 22px;
    color: var(--ink-soft);
  }
</style>
</head>
<body>
  <main class="cover">
    <div class="cover-illustration" role="img" aria-label="Illustration of a businessman riding a unicycle while juggling green dollar signs"></div>
    <h1 class="title">The Quiet<br>Harvest</h1>
    <p class="subtitle">Methods for Steady Savings, Careful Spending, And A Calm Future</p>
    <p class="volume">Volume 1: Foundations</p>
    <p class="author">PK Brenner</p>
  </main>
</body>
</html>
```